One page, two sided flyer about our company needed for a conference

We are an IT consulting company and need a two sided flyer produced for our company that we are going to hand out to potential clients at a conference we have coming up.

We would like the design to be in-line with the look and feel of our current website design: www.brinvaroconsulting.example

Our logo has been attached along with some screenshots from our site that we would like included.

Target Market(s)

Business Executives

Industry/Entity Type

It Company

Font styles to use
Sans Serif

Colors
ec1f27

```html
<!DOCTYPE html>
<html lang="en">
<head>
<meta charset="utf-8">
<title>Brinvaro Consulting – Conference Flyer</title>
<link rel="stylesheet" href="https://fonts.googleapis.com/css2?family=Oswald:wght@400;500;600;700&family=Open+Sans:wght@400;600&display=swap">
<style>
  :root {
    --red: #ec1f27;
    --red-dark: #c9161d;
    --navy: #1b2027;
    --navy-soft: #262c35;
    --ink: #2a2a2a;
    --grey: #6b6b6b;
    --white: #ffffff;
    --stage: #3b3b3d;
  }
  * { box-sizing: border-box; margin: 0; padding: 0; }
  html, body { width: 1200px; height: 776px; overflow: hidden; }
  body { background: var(--stage); font-family: "Open Sans", Arial, sans-serif; position: relative; }

  .flyer { position: absolute; top: 48px; width: 480px; height: 680px; overflow: hidden; }
  .flyer--front { left: 90px; background: var(--navy); }
  .flyer--back { left: 630px; background: var(--white); }

  .brand-name {
    font-family: "Oswald", Arial, sans-serif; font-weight: 600; color: var(--white);
    text-transform: uppercase; letter-spacing: 3px; display: flex; align-items: center; gap: 10px;
  }
  .brand-mark { width: 14px; height: 14px; background: var(--red); display: inline-block; flex: none; }

  /* Front side */
  .front-brand { position: absolute; top: 100px; left: 0; right: 0; justify-content: center; font-size: 34px; }
  .intro-band { position: absolute; top: 166px; left: 0; right: 0; height: 104px; background: var(--white);
    padding: 10px 34px; font-size: 10.2px; line-height: 1.38; color: var(--ink); }
  .front-photo { position: absolute; top: 270px; left: 0; right: 0; height: 272px;
    background: linear-gradient(135deg, #2d333c 0%, #1e232a 55%, #262b33 100%); }
  .services { position: absolute; top: 282px; left: 30px; right: 24px; }
  .service { display: flex; gap: 12px; margin-bottom: 8px; min-height: 72px; }
  .service-hex { flex: 0 0 66px; height: 72px; }
  .service-title { font-family: "Oswald", Arial, sans-serif; font-weight: 700; color: var(--red);
    font-size: 18px; line-height: 1.15; }
  .service-text { color: #e3e3e3; font-size: 10px; line-height: 1.32; }
  .cta { position: absolute; font-family: "Oswald", Arial, sans-serif; font-weight: 600; color: var(--white);
    font-size: 17px; letter-spacing: .5px; padding: 4px 18px; border-radius: 14px; }
  .front-cta { top: 556px; left: 196px; background: var(--red); }
  .contact-row { position: absolute; left: 0; right: 0; display: flex; justify-content: space-around;
    align-items: center; font-family: "Oswald", Arial, sans-serif; font-weight: 500; color: var(--white); font-size: 11.5px; }
  .front-contacts { top: 624px; padding: 0 28px; }
  .contact { display: flex; align-items: center; gap: 5px; white-space: nowrap; }
  .contact svg { width: 15px; height: 15px; flex: none; }

  /* Back side */
  .back-photo { position: absolute; top: 0; left: 0; right: 0; height: 212px;
    background: linear-gradient(120deg, #2f3a45 0%, #5b6470 45%, #8a9098 70%, #4a525c 100%); }
  .back-brand { position: absolute; top: 56px; left: 34px; font-size: 24px; }
  .headline-banner { position: absolute; top: 138px; left: 0; width: 400px; height: 62px; background: var(--red);
    padding: 7px 0 0 26px; color: var(--white); }
  .headline { font-family: "Oswald", Arial, sans-serif; font-weight: 700; font-size: 23px; line-height: 1.1; }
  .subline { font-family: "Oswald", Arial, sans-serif; font-weight: 400; font-size: 15.5px; line-height: 1.2; }
  .section-label { position: absolute; top: 222px; left: 0; right: 0; text-align: center;
    font-family: "Oswald", Arial, sans-serif; font-size: 14px; color: var(--ink); letter-spacing: .5px; }
  .section-rule { position: absolute; top: 246px; left: 30px; right: 30px; height: 1px; background: var(--red); }
  .feature { position: absolute; display: flex; gap: 10px; width: 200px; }
  .feature svg { width: 18px; height: 18px; flex: none; margin-top: 2px; }
  .feature-title { font-family: "Oswald", Arial, sans-serif; font-size: 9.5px; color: var(--ink);
    text-transform: uppercase; letter-spacing: .3px; }
  .feature-text { font-size: 6.6px; line-height: 1.4; color: var(--grey); margin-top: 4px; }
  .feature--devs { top: 268px; left: 24px; }
  .feature--service { top: 262px; left: 250px; width: 206px; }
  .feature--pricing { top: 340px; left: 30px; }
  .back-footer { position: absolute; top: 390px; left: 0; right: 0; bottom: 0; }
  .back-footer svg { display: block; }
  .back-cta { top: 554px; left: 172px; background: var(--navy); }
  .back-contacts { top: 600px; padding: 0 18px; }
</style>
</head>
<body>

<section class="flyer flyer--front">
  <div class="brand-name front-brand"><span class="brand-mark"></span>Brinvaro Consulting</div>

  <p class="intro-band">Brinvaro Consulting was born when experienced service management professionals came together with a single vision: to deliver FlowDesk with a level of customer support that no other company was able or willing to provide. We used our extensive experience and skills to create a startup that could give organizations the IT support they need to achieve their goals. As our IT consultancy firm grows, we retain this commitment to superior customer service.</p>

  <div class="front-photo" role="img" aria-label="Darkened photo of a laptop on a desk"></div>

  <div class="services">
    <div class="service">
      <svg class="service-hex" viewBox="0 0 68 72" aria-hidden="true"><polygon points="34,2 65,19 65,53 34,70 3,53 3,19" fill="var(--red)" stroke="#fff" stroke-width="2.5"/></svg>
      <div><h3 class="service-title">Managed Services</h3>
        <p class="service-text">The key to productivity and efficiency lies in doing only those things which need to be done. But, often companies end-up wasting time struggling with software administration and management.</p></div>
    </div>
    <div class="service">
      <svg class="service-hex" viewBox="0 0 68 72" aria-hidden="true"><polygon points="34,2 65,19 65,53 34,70 3,53 3,19" fill="var(--red)" stroke="#fff" stroke-width="2.5"/></svg>
      <div><h3 class="service-title">Implementation Services</h3>
        <p class="service-text">Starting from scratch is hard and resource-consuming with any system. That's certainly the case with FlowDesk.</p></div>
    </div>
    <div class="service">
      <svg class="service-hex" viewBox="0 0 68 72" aria-hidden="true"><polygon points="34,2 65,19 65,53 34,70 3,53 3,19" fill="var(--red)" stroke="#fff" stroke-width="2.5"/></svg>
      <div><h3 class="service-title">Managed Services</h3>
        <p class="service-text">FlowDesk is officially live for your team. The scope and initial deployment is done – your company is excited … Now what? Whether you need experts to support your over-burdened Admin team, or a kick-start to enhance your company's instance, we can help you gain back business momentum and ensure…</p></div>
    </div>
  </div>

  <div class="cta front-cta">GET IN TOUCH</div>

  <div class="contact-row front-contacts">
    <span class="contact"><svg viewBox="0 0 16 16"><rect width="16" height="16" rx="3" fill="var(--red)"/><path d="M5 3.5l2 2.2-1 1.2c.6 1.3 1.6 2.3 2.9 2.9l1.2-1 2.2 2-1.1 1.6C7.6 12.2 3.8 8.4 3.5 4.6z" fill="#fff"/></svg>555.010.4821</span>
    <span class="contact"><svg viewBox="0 0 16 16"><rect width="16" height="16" rx="3" fill="var(--red)"/><rect x="3" y="4.5" width="10" height="7" fill="none" stroke="#fff" stroke-width="1.2"/><path d="M3 4.5l5 4 5-4" fill="none" stroke="#fff" stroke-width="1.2"/></svg>info@brinvaroconsulting.example</span>
    <span class="contact"><svg viewBox="0 0 16 16"><rect width="16" height="16" rx="3" fill="var(--red)"/><circle cx="8" cy="8" r="5" fill="none" stroke="#fff" stroke-width="1.1"/><path d="M3 8h10M8 3c-2.5 3-2.5 7 0 10M8 3c2.5 3 2.5 7 0 10" fill="none" stroke="#fff" stroke-width="1"/></svg>www.brinvaroconsulting.example</span>
  </div>
</section>

<section class="flyer flyer--back">
  <div class="back-photo" role="img" aria-label="Photo of business people walking through a glass office building"></div>
  <div class="brand-name back-brand"><span class="brand-mark"></span>Brinvaro Consulting</div>

  <div class="headline-banner">
    <h1 class="headline">IT STRATEGY AND IMPLEMENTATION</h1>
    <p class="subline">We take your company to the cutting edge of efficiency</p>
  </div>

  <h2 class="section-label">WHAT WE DO</h2>
  <div class="section-rule"></div>

  <div class="feature feature--devs">
    <svg viewBox="0 0 18 18" aria-hidden="true"><circle cx="9" cy="9" r="7.5" fill="none" stroke="var(--red)" stroke-width="1.5"/><path d="M5.5 9.2l2.4 2.3 4.6-4.8" fill="none" stroke="var(--red)" stroke-width="1.6"/></svg>
    <div><h3 class="feature-title">Experienced Solution Focused Developers</h3>
      <p class="feature-text">All Of Our Developers Have Vast Amounts Of Experience In FlowDesk</p></div>
  </div>
  <div class="feature feature--service">
    <svg viewBox="0 0 18 18" aria-hidden="true"><circle cx="9" cy="9" r="7.5" fill="none" stroke="var(--red)" stroke-width="1.5"/><path d="M5.5 9.2l2.4 2.3 4.6-4.8" fill="none" stroke="var(--red)" stroke-width="1.6"/></svg>
    <div><h3 class="feature-title">Superior Service</h3>
      <p class="feature-text">Our Customers Come First And Our Client Retention Rate Of 98% Proves It. From Word One You Are Our Focus. Whether It Is Providing Alternative Solutions That No One Has Explored, Working With You On A Projects Price, Delivering A Finished Product By A Certain Date Etc.</p></div>
  </div>
  <div class="feature feature--pricing">
    <svg viewBox="0 0 18 18" aria-hidden="true"><circle cx="9" cy="9" r="7.5" fill="none" stroke="var(--red)" stroke-width="1.5"/><path d="M5.5 9.2l2.4 2.3 4.6-4.8" fill="none" stroke="var(--red)" stroke-width="1.6"/></svg>
    <div><h3 class="feature-title">Competitive Pricing</h3>
      <p class="feature-text">All Solutions Are Presented With Several Delivery Options E.G Full-Time US Developers, A Hybrid Of US + Near Shore, Or All Near Shore.</p></div>
  </div>

  <div class="back-footer">
    <svg width="480" height="290" viewBox="0 0 480 290" role="img" aria-label="Red-tinted photo of an office desk from above">
      <defs><linearGradient id="deskTint" x1="0" y1="0" x2="1" y2="1"><stop offset="0" stop-color="var(--red)"/><stop offset="1" stop-color="var(--red-dark)"/></linearGradient></defs>
      <rect width="480" height="290" fill="url(#deskTint)"/>
      <polygon points="0,0 480,0 480,50 300,80 0,90" fill="#fff"/>
    </svg>
  </div>

  <div class="cta back-cta">GET IN TOUCH</div>

  <div class="contact-row back-contacts">
    <span class="contact"><svg viewBox="0 0 16 16"><path d="M5 3.5l2 2.2-1 1.2c.6 1.3 1.6 2.3 2.9 2.9l1.2-1 2.2 2-1.1 1.6C7.6 12.2 3.8 8.4 3.5 4.6z" fill="var(--navy)"/></svg>555.010.4821</span>
    <span class="contact"><svg viewBox="0 0 16 16"><rect x="2" y="4" width="12" height="8" fill="none" stroke="var(--navy)" stroke-width="1.4"/><path d="M2 4l6 4.5L14 4" fill="none" stroke="var(--navy)" stroke-width="1.4"/></svg>info@brinvaroconsulting.example</span>
    <span class="contact"><svg viewBox="0 0 16 16"><circle cx="8" cy="8" r="6" fill="none" stroke="var(--navy)" stroke-width="1.3"/><path d="M2 8h12M8 2c-3 3.5-3 8.5 0 12M8 2c3 3.5 3 8.5 0 12" fill="none" stroke="var(--navy)" stroke-width="1.1"/></svg>www.brinvaroconsulting.example</span>
  </div>
</section>

</body>
</html>
```